Kestrel Harbor is a Smart Device integration/installation business

Hi, I am a tech enthusiast with a background in robotics, industrial automation and computers. I have currently launched a business to bring wireless voice controlled devices and smart devices into peoples homes at affordable prices, moving away from expensive smart wiring and programming installations. I fix bad wifi in houses and install new smart locks, multi-room audio, automated blinds etc. that can all be controlled through velma (brindle) or Pimbro Nest.

I need a modern and eye catching a5 flyer developed for post box drops that give people an understanding of what smart devices are - pimbro nest, brindle velma etc and how it can improve their lives. I have a couple of examples that I put together before realising that I need professional help. So please use these as a guide if they are helpful.

My website which also needs some work is: www.kestrelharbor.net for some more ideas and info on the services I supply. I also have a facebook page with that business name for some recent posts.

Logos as attached.

If you need anymore info or idea on what I do let me know, cheers.

Target Market(s)

Pre-exisiting homes

Industry/Entity Type

Technology Equipment

Requirements
Must have
• My logo and business details mob and website

```html
<!DOCTYPE html>
<html lang="en">
<head>
<meta charset="utf-8">
<title>Kestrel Harbor – Smart Home Flyer</title>
<link href="https://fonts.googleapis.com/css2?family=Lato:wght@400;700;900&family=Roboto+Condensed:wght@400;700&display=swap" rel="stylesheet">
<style>
  :root{
    --bg:#aaaaaa;
    --paper:#ffffff;
    --blue:#1f6fb2;
    --blue-deep:#15467f;
    --blue-head:#1d4f8f;
    --ink:#2b2b2b;
    --text:#3a3a3a;
    --grey-ring:#c4c4c4;
    --black-ring:#161616;
  }
  *{margin:0;padding:0;box-sizing:border-box}
  html,body{width:1200px;height:1200px;overflow:hidden}
  body{background:var(--bg);position:relative;font-family:'Lato',sans-serif;color:var(--text)}
  .page{position:absolute;width:497px;height:706px;background:var(--paper);overflow:hidden}
  .page--front{left:71px;top:267px}
  .page--back{left:633px;top:266px}

  /* front */
  .hero-art{position:absolute;left:0;top:0}
  .hero-copy{position:absolute;left:20px;top:30px;width:230px;color:#fff}
  .hero-title{font-family:'Roboto Condensed',sans-serif;line-height:1}
  .hero-title .line-a{display:block;font-size:23px;font-weight:400;color:#fff;letter-spacing:.3px}
  .hero-title .line-a b{font-weight:700}
  .hero-title .line-b{display:block;font-size:28px;font-weight:700;color:#1a1a1a;margin-top:7px}
  .hero-title .line-c{display:block;font-size:28px;font-weight:700;color:#fff;margin-top:6px}
  .hero-lead{font-size:12px;line-height:14.2px;margin-top:10px;text-align:justify;width:194px}
  .hero-price{font-family:'Roboto Condensed',sans-serif;font-weight:700;font-size:33px;margin-top:10px}
  .product-tag{position:absolute;font-family:'Roboto Condensed',sans-serif;font-weight:700;font-size:11px;color:#1f6fb2;background:rgba(255,255,255,.75);padding:0 3px}

  .brand{position:absolute;left:0;width:100%;top:300px;display:flex;align-items:center;justify-content:center;gap:10px}
  .brand-dot{width:44px;height:44px;border-radius:50%;background:var(--blue-deep)}
  .brand-name{font-family:'Lato',sans-serif;font-weight:700;font-size:26px;color:var(--blue-deep)}

  .faq{position:absolute;top:367px;width:194px}
  .faq--left{left:31px}
  .faq--right{left:266px}
  .faq h3{font-size:11.5px;font-weight:700;color:var(--blue-head);margin-bottom:4px}
  .faq p{font-size:10.4px;line-height:12.8px;text-align:justify;color:#333}

  .family-photo{position:absolute;left:0;top:493px;width:100%;height:213px;
    background:linear-gradient(100deg,#eef1f4 0%,#c7a690 30%,#d9c4b0 55%,#b89780 75%,#6a6f78 100%)}
  .footer-band{position:absolute;left:0;bottom:0;width:100%;height:24px;
    background:linear-gradient(90deg,rgba(20,40,70,.55),rgba(20,50,90,.85),rgba(20,40,70,.55));
    color:#fff;text-align:center;font-size:12px;letter-spacing:2.4px;line-height:24px}

  /* back */
  .back-header{position:absolute;left:0;top:14px;width:100%;height:60px;
    background:linear-gradient(180deg,#2a7fc4,var(--blue-deep));color:#fff;
    font-family:'Lato',sans-serif;font-weight:700;font-size:14.4px;line-height:17px;
    padding:14px 19px 0;text-transform:uppercase;text-align:justify;text-align-last:left}
  .ring-row{position:absolute;left:0;width:100%}
  .ring-row--one{top:110px}
  .ring-row--two{top:311px}
  .ring-row svg{display:block}
  .ring-label{position:absolute;width:120px;text-align:center;font-size:14.6px;line-height:17px;color:#333;font-weight:400}

  .device-art{position:absolute;left:18px;top:513px;width:150px;height:160px}
  .offer{position:absolute;left:178px;top:537px;width:304px}
  .offer p{font-size:10.2px;line-height:12.8px;text-align:justify;color:#444}
  .offer .cta{font-weight:700;color:var(--blue-head);font-size:10.6px;margin-top:8px}
  .contact{margin-top:6px;list-style:none}
  .contact li{display:flex;align-items:center;gap:8px;font-size:12px;color:#333;height:20px}
  .contact li.phone{font-family:'Roboto Condensed',sans-serif;font-weight:700;font-size:17px;color:#111}
  .contact svg{flex:none}
</style>
</head>
<body>

<!-- FRONT PAGE -->
<section class="page page--front">
  <svg class="hero-art" width="497" height="290" viewBox="0 0 497 290">
    <defs>
      <linearGradient id="panelBlue" x1="0" y1="0" x2="0" y2="1">
        <stop offset="0" stop-color="#2f87c8"/>
        <stop offset="1" stop-color="#173f78"/>
      </linearGradient>
    </defs>
    <polygon points="0,18 334,18 228,274 0,274" fill="url(#panelBlue)"/>
    <polygon role="img" aria-label="Photo of a smart speaker on a table" points="368,10 497,10 497,105 410,105" fill="#d9d5cf"/>
    <polygon role="img" aria-label="Photo of a hand touching a round smart speaker" points="338,36 398,34 440,96 402,150 248,142" fill="#5f6469"/>
    <polygon role="img" aria-label="Photo of a tall cylindrical smart speaker" points="245,165 330,172 352,273 232,273" fill="#e4e4e2"/>
    <circle role="img" aria-label="Photo of three smart speakers side by side on a dark background" cx="421" cy="210" r="102" fill="#1c1c1e" stroke="#fff" stroke-width="4"/>
  </svg>
  <span class="product-tag" style="left:403px;top:36px">Pimbro Nest</span>
  <span class="product-tag" style="left:284px;top:105px">Orchard Pod</span>
  <span class="product-tag" style="left:254px;top:224px">Brindle Chime</span>

  <div class="hero-copy">
    <h1 class="hero-title">
      <span class="line-a">YOUR <b>SMART HOME</b></span>
      <span class="line-b">INTEGRATION</span>
      <span class="line-c">PROFESSIONALS</span>
    </h1>
    <p class="hero-lead">We'll show you how these speaker powered voice activated Smart Assitants hold the key to your New Smart Home. Start building your new Smart Home with these devices starting from</p>
    <p class="hero-price">$50.00</p>
  </div>

  <div class="brand">
    <span class="brand-dot"></span>
    <span class="brand-name">Kestrel Harbor</span>
  </div>

  <article class="faq faq--left">
    <h3>What exactacly is a Smart Assistant?</h3>
    <p>Like Lumi, Corvin or Pimbro Assistant on your smartphone, except for your home. An unpaid personal assitant doing all mundane tasks around your home. Combining these vitual assitants with speaker hardware allows you to turn your home into an automated, voice activated, app-controlled hub.</p>
  </article>
  <article class="faq faq--right">
    <h3>Why do I need Smart Devices?</h3>
    <p>If you are happy turning your own electrical equipment on and finding the remote for the tv or walking to the other side of the house because you left the light on - you don't. But if you prefer to spend more time with you family, pets or leisure activities, Smart devices are your answer.</p>
  </article>

  <div class="family-photo" role="img" aria-label="Photo of a family relaxing together on a sofa looking at a phone"></div>
  <div class="footer-band">kestrelharbor.net</div>
</section>

<!-- BACK PAGE -->
<section class="page page--back">
  <header class="back-header">Our smart devices offer security, convience, save you money and leave you time for more important things</header>

  <div class="ring-row ring-row--one">
    <svg width="497" height="135" viewBox="0 0 497 135">
      <g fill="none" stroke-width="9">
        <circle cx="81" cy="67" r="56" stroke="var(--grey-ring)"/>
        <path d="M25 67 A56 56 0 0 1 137 67" stroke="var(--blue)"/>
        <circle cx="191" cy="67" r="56" stroke="var(--grey-ring)"/>
        <path d="M247 67 A56 56 0 0 1 135 67" stroke="var(--black-ring)"/>
        <circle cx="303" cy="67" r="56" stroke="var(--grey-ring)"/>
        <path d="M247 67 A56 56 0 0 1 359 67" stroke="var(--blue)"/>
        <circle cx="418" cy="67" r="56" stroke="var(--grey-ring)"/>
        <path d="M474 67 A56 56 0 0 1 362 67" stroke="var(--black-ring)"/>
      </g>
      <circle role="img" aria-label="Photo of a living room with a wall mounted TV" cx="81" cy="67" r="46" fill="#8a7f78"/>
      <circle role="img" aria-label="Photo of a smart speaker on a shelf" cx="191" cy="67" r="46" fill="#c9d3dc"/>
      <circle role="img" aria-label="Photo of a security camera app on a phone" cx="303" cy="67" r="46" fill="#b7b2ac"/>
      <circle role="img" aria-label="Photo of a video doorbell at a front door" cx="418" cy="67" r="46" fill="#a9aeb2"/>
    </svg>
    <span class="ring-label" style="left:21px;top:145px">Multi-Room<br>Audio</span>
    <span class="ring-label" style="left:131px;top:145px">Voice<br>Assistant</span>
    <span class="ring-label" style="left:243px;top:145px">Smart CCTV</span>
    <span class="ring-label" style="left:364px;top:145px;width:120px">Video Doorbell</span>
  </div>

  <div class="ring-row ring-row--two">
    <svg width="497" height="135" viewBox="0 0 497 135">
      <g fill="none" stroke-width="9">
        <circle cx="81" cy="67" r="56" stroke="var(--grey-ring)"/>
        <path d="M25 67 A56 56 0 0 1 137 67" stroke="var(--blue)"/>
        <circle cx="191" cy="67" r="56" stroke="var(--grey-ring)"/>
        <path d="M247 67 A56 56 0 0 1 135 67" stroke="var(--black-ring)"/>
        <circle cx="303" cy="67" r="56" stroke="var(--grey-ring)"/>
        <path d="M247 67 A56 56 0 0 1 359 67" stroke="var(--blue)"/>
        <circle cx="418" cy="67" r="56" stroke="var(--grey-ring)"/>
        <path d="M474 67 A56 56 0 0 1 362 67" stroke="var(--black-ring)"/>
      </g>
      <circle role="img" aria-label="Photo of window blinds with a motor unit" cx="81" cy="67" r="46" fill="#dcdcdc"/>
      <circle role="img" aria-label="Photo of a car in front of a garage door" cx="191" cy="67" r="46" fill="#8d9399"/>
      <circle role="img" aria-label="Photo of a kitchen with coloured lighting" cx="303" cy="67" r="46" fill="#6e4a64"/>
      <circle role="img" aria-label="Photo of a hand unlocking a smart lock" cx="418" cy="67" r="46" fill="#9c9d9a"/>
    </svg>
    <span class="ring-label" style="left:21px;top:145px">Smart Blinds</span>
    <span class="ring-label" style="left:131px;top:145px">Smart Garage</span>
    <span class="ring-label" style="left:243px;top:145px">Lighting<br>Control</span>
    <span class="ring-label" style="left:358px;top:145px">Smart Locks</span>
  </div>

  <svg class="device-art" viewBox="0 0 150 160">
    <ellipse role="img" aria-label="Photo of a round network security device" cx="40" cy="125" rx="40" ry="25" fill="#3aa3dc"/>
    <rect role="img" aria-label="Photo of a phone showing a parental control app" x="80" y="0" width="70" height="150" rx="9" fill="#eef2f6" stroke="#c9ced3" stroke-width="2"/>
    <rect x="66" y="100" width="32" height="42" rx="3" fill="#1d3c6e"/>
  </svg>

  <div class="offer">
    <p>KH is now offering ‘Wardbox’ - a device protecting your home and privacy from external threats. Your gateway to user friendly parental control. Monitor usage, schedule access, remote notifications when devices connect plus many more features. Sounds complicated? Let us show you how easy it really is.</p>
    <p class="cta">Contact us to find out how we can help you.</p>
    <ul class="contact">
      <li class="phone">
        <svg width="12" height="12" viewBox="0 0 24 24"><path fill="#1d4f8f" d="M6.6 10.8a15 15 0 0 0 6.6 6.6l2.2-2.2a1 1 0 0 1 1-.25 11.4 11.4 0 0 0 3.6.57 1 1 0 0 1 1 1V20a1 1 0 0 1-1 1A17 17 0 0 1 3 4a1 1 0 0 1 1-1h3.5a1 1 0 0 1 1 1c0 1.25.2 2.45.57 3.57a1 1 0 0 1-.25 1z"/></svg>
        0491 570 156
      </li>
      <li>
        <svg width="12" height="12" viewBox="0 0 24 24"><path fill="#1d4f8f" d="M2 5h20v14H2z"/><path fill="none" stroke="#fff" stroke-width="2" d="M2 6l10 7 10-7"/></svg>
        info@kestrelharbor.net
      </li>
      <li>
        <svg width="12" height="12" viewBox="0 0 24 24"><circle cx="12" cy="12" r="10" fill="#1d4f8f"/><path fill="none" stroke="#fff" stroke-width="1.5" d="M2 12h20M12 2c3 3 3 17 0 20M12 2c-3 3-3 17 0 20"/></svg>
        kestrelharbor.net
      </li>
    </ul>
  </div>
</section>

</body>
</html>
```